Circuit Dominion book cover

I need a front book cover design for my book titled "Circuit Dominion: The Gilded Gift of Planetary Upheaval". It is a non-fiction book 5.5 x 8.5 paperback. The topic concerns Technocracy, where all elements of society are controlled by scientists, engineers and other experts, using science and technology as the rationale for making all decisions pertaining to people's lives. Using a Trojan horse could be OK, but some imagery for technology would be necessary. This is a sophisticated book, however, and I want a classy and clean looking cover that is not overly-sensationalistic or cluttered. The subtitle could tuck nicely underneath the main title, Circuit Dominion. The rest of the cover (spine, back and inside) will be completed by my publisher.

```html
<!DOCTYPE html>
<html lang="en">
<head>
<meta charset="utf-8">
<title>Circuit Dominion: The Gilded Gift of Planetary Upheaval — Front Cover</title>
<link rel="stylesheet" href="https://fonts.googleapis.com/css2?family=Josefin+Sans:wght@300;400&display=swap">
<style>
  :root {
    --stage: #4f7d7e;
    --cover-top: #34bfe6;
    --cover-bottom: #1c9dd1;
    --ink: #1f2a33;
    --title: #ffffff;
    --subtitle: #d6f3fb;
    --rule: #ffffff;
    --monitor-frame: #f2f2f2;
    --monitor-screen: #f28a1e;
    --tablet-frame: #3b4a55;
    --tablet-screen: #4bb3ec;
    --phone-frame: #8fd0ee;
    --phone-screen: #4cc34a;
  }
  * { margin: 0; padding: 0; box-sizing: border-box; }
  html, body {
    width: 1200px;
    height: 795px;
    overflow: hidden;
    background: var(--stage);
  }
  .stage {
    position: relative;
    width: 1200px;
    height: 795px;
    display: flex;
    align-items: center;
    justify-content: center;
  }
  .cover {
    position: relative;
    width: 453px;
    height: 700px;
    background: linear-gradient(170deg, var(--cover-top), var(--cover-bottom));
    box-shadow: 0 18px 40px rgba(0, 0, 0, 0.25);
    overflow: hidden;
  }
  .cover__heading {
    position: absolute;
    left: 44px;
    top: 70px;
    padding-left: 14px;
    border-left: 2px solid var(--rule);
    font-family: "Josefin Sans", sans-serif;
    font-weight: 300;
    text-transform: uppercase;
    letter-spacing: 0.12em;
  }
  .cover__title {
    color: var(--title);
    font-size: 25px;
    font-weight: 400;
    line-height: 1.15;
  }
  .cover__subtitle {
    color: var(--subtitle);
    font-size: 15px;
    line-height: 1.2;
    margin-top: 4px;
  }
  .cover__art {
    position: absolute;
    left: 0;
    top: 0;
    width: 453px;
    height: 700px;
  }
</style>
</head>
<body>
  <main class="stage">
    <article class="cover">
      <h1 class="cover__heading">
        <span class="cover__title">Circuit Dominion:</span><br>
        <span class="cover__subtitle">The Gilded Gift of<br>Planetary Upheaval</span>
      </h1>

      <svg class="cover__art" viewBox="0 0 453 700" xmlns="http://www.w3.org/2000/svg">
        <!-- network wiring -->
        <g fill="none" stroke="var(--ink)" stroke-width="2">
          <polyline points="150,390 90,390 90,470"/>
          <polyline points="270,260 330,260 330,310"/>
          <polyline points="290,370 340,370 340,410"/>
        </g>

        <!-- trojan horse on wheeled platform -->
        <rect class="horse" x="130" y="200" width="170" height="210" rx="6"
              fill="var(--ink)" opacity="0.9"
              role="img" aria-label="Flat silhouette of a wooden Trojan horse standing on a wheeled platform"/>

        <!-- desktop monitor -->
        <g class="device device--monitor">
          <rect x="70" y="450" width="210" height="140" rx="4" fill="var(--monitor-frame)"/>
          <rect x="80" y="460" width="190" height="112" fill="var(--monitor-screen)"/>
          <rect x="160" y="590" width="30" height="28" fill="var(--monitor-frame)"/>
          <rect x="135" y="616" width="80" height="8" rx="2" fill="var(--monitor-frame)"/>
        </g>

        <!-- tablet -->
        <g class="device device--tablet">
          <rect x="300" y="410" width="120" height="95" rx="6" fill="var(--tablet-frame)"/>
          <rect x="308" y="418" width="104" height="79" fill="var(--tablet-screen)"/>
        </g>

        <!-- phone -->
        <g class="device device--phone">
          <rect x="310" y="310" width="60" height="44" rx="5" fill="var(--phone-frame)"/>
          <rect x="316" y="315" width="48" height="34" fill="var(--phone-screen)"/>
        </g>
      </svg>
    </article>
  </main>
</body>
</html>
```